website design for a new age Real Estate Security Business

We are launching a business in real estate which no body else is doing. We are going to use technology in terms of software and hardware to provide our services.

We are going to use Big Data, IOT etc.. for our services.

NOTE: We don't want to see Shiel or buildings etc.. that directly suggests Real estate or security on this design

Target Market(s)

India

Industry/Entity Type

Real Estate

Number of Pages Required

4 page

Font styles to use
Sans Serif
Other font styles liked:
• Use Google Fonts

Requirements
Must have
• Home Page should be trendy and colourful should give user confidence to subscribe to our service.
Nice to have
• Use Google fonts.
Should not have
• Design shouldnt have Shield or Buildings that directly suggests real estate or security.

```html
<!DOCTYPE html>
<html lang="en">
<head>
<meta charset="utf-8">
<title>Plotwise Guard</title>
<link rel="stylesheet" href="https://fonts.googleapis.com/css2?family=Roboto:ital,wght@0,100;0,300;0,400;0,500;0,700;0,900;1,900&family=Roboto+Condensed:ital,wght@0,400;0,700;1,700&display=swap">
<style>
:root{
  --red:#d0300f;
  --red-dark:#b02408;
  --blue:#1a78c2;
  --blue-dark:#0f5fa3;
  --navy:#07131d;
  --ink:#111;
  --text:#333;
  --pale-blue:#dcecfa;
  --charcoal:#2b2b2b;
  --field:#333;
  --white:#fff;
}
*{margin:0;padding:0;box-sizing:border-box}
html,body{width:1200px;height:3020px;overflow:hidden}
body{position:relative;background:var(--white);font-family:'Roboto',sans-serif;color:var(--text)}
.abs{position:absolute}

/* header */
.site-header{left:0;top:0;width:1200px;height:64px;background:var(--white);border-top:3px solid var(--navy)}
.brand{left:161px;top:14px;font:700 26px/32px 'Roboto',sans-serif;color:var(--red)}
.nav{left:656px;top:17px;display:flex;gap:6px;align-items:center}
.nav a{font:500 13px/1 'Roboto',sans-serif;color:var(--ink);text-decoration:none;padding:8px 14px}
.nav a.active{border:2px solid var(--red);margin-right:4px}
.cart-link{position:relative;width:22px;height:22px;margin-left:16px}
.cart-badge{position:absolute;right:-8px;top:-8px;width:14px;height:14px;border-radius:50%;background:var(--red);color:#fff;font:700 8px/14px 'Roboto',sans-serif;text-align:center}

/* hero */
.hero{left:0;top:64px;width:1200px;height:466px;background:var(--navy);overflow:hidden}
.hero-art{position:absolute;left:0;top:0;width:1200px;height:466px;
  background:radial-gradient(ellipse 360px 280px at 360px 210px,rgba(42,140,220,.45),rgba(208,48,15,.25) 50%,transparent 75%),
             radial-gradient(ellipse 200px 160px at 1100px 60px,rgba(42,140,220,.25),transparent 70%),var(--navy)}
.hero-copy{position:absolute;right:56px;top:190px;text-align:right}
.hero-line{font:300 42px/1 'Roboto',sans-serif;color:#2a9fe6;letter-spacing:1px}
.hero-big{font:italic 700 104px/0.95 'Roboto Condensed',sans-serif;color:var(--red);margin:4px 0 2px}

/* tagline band */
.tag-band{left:0;top:530px;width:1200px;height:64px;background:var(--red)}
.tag-band h2{position:absolute;left:161px;top:20px;font:700 21px/24px 'Roboto',sans-serif;color:#fff}
.btn-dark{position:absolute;left:914px;top:12px;width:123px;height:38px;background:#111;color:#fff;font:700 12px/38px 'Roboto',sans-serif;text-align:center}

.arrow-dot{display:inline-block;width:11px;height:11px;border-radius:50%;vertical-align:-1px;margin-left:5px;background:currentColor;position:relative}
.arrow-dot::after{content:"";position:absolute;left:3px;top:3px;border-left:5px solid #111;border-top:2.5px solid transparent;border-bottom:2.5px solid transparent}
.btn-outline .arrow-dot::after{border-left-color:#fff}

/* services */
.eyebrow{left:502px;top:636px;font:400 13px/16px 'Roboto',sans-serif;color:var(--ink)}
.eyebrow::after{content:"";position:absolute;left:100px;top:8px;width:94px;height:1px;background:var(--blue)}
.section-title{left:0;width:1200px;top:652px;text-align:center;font:500 26px/30px 'Roboto',sans-serif;color:var(--blue)}
.section-lead{left:195px;top:696px;width:810px;text-align:center;font:400 11px/20px 'Roboto',sans-serif;color:#444}

.service-photo{height:258px;top:761px;width:425px}
.photo-doc{left:161px;background:linear-gradient(120deg,#dfe7ef 0%,#6b87a6 25%,#12233a 55%,#0a1626 100%)}
.photo-land{left:612px;background:linear-gradient(135deg,#9db8d8 0%,#5f82ad 40%,#2d4a73 75%,#1b2f4e 100%)}
.service-card{top:970px;width:281px;height:177px;background:var(--pale-blue);border-top:5px solid var(--blue);text-align:center}
.card-doc{left:240px}.card-land{left:690px}
.service-card h3{margin-top:20px;font:700 20px/24px 'Roboto',sans-serif;color:var(--ink)}
.service-card p{margin:12px auto 0;width:240px;font:400 11px/17px 'Roboto',sans-serif;color:#333}
.btn-outline{display:inline-block;margin-top:12px;border:2px solid #222;padding:0 10px;height:30px;font:500 10px/26px 'Roboto',sans-serif;color:#222}
.btn-outline .arrow-dot{background:#222}

/* welcome */
.welcome{left:161px;top:1204px;width:431px;height:330px;background:var(--pale-blue);padding:28px 24px 0 24px}
.welcome h2{font:700 22px/26px 'Roboto',sans-serif;color:var(--ink)}
.welcome h2 .c-red{color:var(--red)}.welcome h2 .c-blue{color:var(--blue)}
.welcome p{margin-top:14px;font:400 11px/17.5px 'Roboto',sans-serif;color:#222;text-align:justify}
.welcome .btn-outline{margin-top:18px}
.welcome-photo{left:602px;top:1204px;width:437px;height:330px;background:linear-gradient(110deg,#eef1f4 0%,#cdd6de 35%,#8a98a6 60%,#d7dde2 100%)}

/* process */
.process{left:0;top:1594px;width:1200px;height:190px;background:linear-gradient(180deg,#16222a,#0c1419)}
.process svg{position:absolute;left:0;top:0}
.step-label{position:absolute;top:142px;width:160px;text-align:center;font:500 15px/18px 'Roboto',sans-serif;color:#fff}

/* pricing */
.price-title{left:0;width:1200px;top:1832px;text-align:center;font:700 34px/40px 'Roboto',sans-serif;color:var(--ink)}
.plan{top:1924px;width:403px;height:532px;border:2px solid;border-radius:10px;overflow:hidden;background:
  repeating-linear-gradient(0deg,transparent 0 29px,rgba(0,0,0,.04) 29px 30px),
  repeating-linear-gradient(90deg,transparent 0 29px,rgba(0,0,0,.04) 29px 30px),#f7f7f7;text-align:center}
.plan-doc{left:181px;border-color:var(--red)}
.plan-land{left:616px;border-color:var(--blue)}
.plan-head{height:100px;color:#fff;font:500 27px/100px 'Roboto',sans-serif}
.plan-doc .plan-head{background:var(--red)}
.plan-land .plan-head{background:var(--blue)}
.plan-badge{position:relative;margin:24px auto 0;width:116px;height:116px}
.plan-badge svg{position:absolute;left:0;top:0}
.plan-badge span{position:absolute;left:0;top:0;width:116px;height:116px;font:700 28px/116px 'Roboto',sans-serif;color:#fff;text-align:center}
.per-month{margin-top:16px;font:700 22px/26px 'Roboto',sans-serif;color:var(--ink)}
.plan ul{list-style:none;margin:16px 0 0 90px;text-align:left}
.plan li{font:400 13px/25px 'Roboto',sans-serif;color:#222}
.plan li svg{vertical-align:-2px;margin-right:8px}
.order-btn{position:relative;margin:22px auto 0;width:206px;height:57px;border-radius:29px;color:#fff;font:700 20px/57px 'Roboto',sans-serif;text-align:left;padding-left:44px}
.plan-doc .order-btn{background:linear-gradient(180deg,#e8431d,var(--red-dark))}
.plan-land .order-btn{background:linear-gradient(180deg,#2a8ad6,var(--blue-dark))}
.order-btn i{position:absolute;right:6px;top:7px;width:43px;height:43px;border-radius:50%;background:#fff}
.order-btn svg{position:absolute;left:11px;top:11px}

/* contact */
.contact{left:0;top:2527px;width:1200px;height:440px;background:radial-gradient(ellipse at 50% 40%,#303030,#222 80%)}
.contact-icon{position:absolute;left:568px;top:32px;width:64px;height:64px;border-radius:50%;background:var(--blue)}
.contact-icon svg{position:absolute;left:16px;top:18px}
.contact h2{position:absolute;left:0;width:1200px;top:108px;text-align:center;font:700 34px/40px 'Roboto Condensed',sans-serif;color:#ddd;letter-spacing:-1.5px}
.field{position:absolute;top:173px;height:30px;background:var(--field);border:1px solid #4a4a4a;border-radius:3px;font:400 10px/28px 'Roboto',sans-serif;color:#bbb;padding-left:38px}
.field svg{position:absolute;left:10px;top:8px}
.f-name{left:171px;width:280px}.f-phone{left:465px;width:278px}.f-mail{left:759px;width:272px}
.f-msg{position:absolute;left:171px;top:217px;width:860px;height:115px;background:var(--field);border:1px solid #4a4a4a;border-radius:3px;font:400 10px/14px 'Roboto',sans-serif;color:#bbb;padding:14px 12px}
.submit{position:absolute;left:550px;top:368px;width:114px;height:36px;background:var(--blue);color:#fff;font:700 15px/36px 'Roboto',sans-serif;text-align:center}

.site-footer{left:0;top:2967px;width:1200px;height:53px;background:var(--red);text-align:center;font:400 11px/53px 'Roboto',sans-serif;color:#fff}
</style>
</head>
<body>

<header class="abs site-header">
  <div class="abs brand">Plotwise Guard</div>
  <nav class="abs nav">
    <a class="active">HOME</a>
    <a>SERVICES</a>
    <a>PRICING</a>
    <a>CONTACT US</a>
    <span class="cart-link">
      <svg width="16" height="16" viewBox="0 0 16 16"><path d="M1 2h3l2 8h7l2-6H5" fill="none" stroke="#111" stroke-width="2"/><circle cx="7" cy="13.5" r="1.5" fill="#111"/><circle cx="12" cy="13.5" r="1.5" fill="#111"/></svg>
      <span class="cart-badge">0</span>
    </span>
  </nav>
</header>

<section class="abs hero">
  <div class="hero-art" role="img" aria-label="Abstract data visualisation of flowing red and blue particle lines on a dark background"></div>
  <div class="hero-copy">
    <div class="hero-line">ADVANCED ANALYTICS</div>
    <div class="hero-big">BIG DATA</div>
    <div class="hero-line">AND VISUALIZATION</div>
  </div>
</section>

<section class="abs tag-band">
  <h2>TO KEEP YOUR PROPERTY SAFE AND SECURITY</h2>
  <a class="btn-dark">LEARN MORE <span class="arrow-dot" style="background:#fff"></span></a>
</section>

<div class="abs eyebrow">OUR SERVICES</div>
<h2 class="abs section-title">WHAT WE OFFER</h2>
<p class="abs section-lead">Lorem Ipsum is simply dummy text of the printing and typesetting industry. Lorem Ipsum has been the industry's standard dummy survived not only five centuries, but also the leap into electronic typesetting, remaining essentially unchanged. It was popularised software like Pagewright Studio including versions of Lorem Ipsum.</p>

<div class="abs service-photo photo-doc" role="img" aria-label="Hand touching a screen full of code"></div>
<div class="abs service-photo photo-land" role="img" aria-label="Surveillance camera beside a model house"></div>

<article class="abs service-card card-doc">
  <h3>DOC SECURE</h3>
  <p>Lorem Ipsum is simply dummy text of the printing the industry's standard dummy text ever since the type and scrambled it.</p>
  <a class="btn-outline">READ MORE <span class="arrow-dot"></span></a>
</article>
<article class="abs service-card card-land">
  <h3>LAND SECURE</h3>
  <p>Lorem Ipsum is simply dummy text of the printing the industry's standard dummy text ever since the type and scrambled it.</p>
  <a class="btn-outline">READ MORE <span class="arrow-dot"></span></a>
</article>

<section class="abs welcome">
  <h2>WELCOME TO <span class="c-red">PLOTWISE</span> <span class="c-blue">GUARD</span></h2>
  <p>Lorem Ipsum is simply dummy text of the printing and typesetting industry. Lorem Ipsum has been the industry's standard dummy text ever since the 1500s, when an unknown printer took a galley of type and scrambled it to make a type specimen book. It has survived not only five centuries, but also the leap into electronic with the release of Lexaprint sheets containing Lorem Ipsum passages, and more versions of Lorem Ipsum.</p>
  <p>Lorem Ipsum is simply dummy text of the printing and typesetting industry. Lorem unknown printer took a galley of type and scrambled it to make a type specimen book. It has survived not only five centuries, but also the leap into electronic with versions of Lorem Ipsum.</p>
  <a class="btn-outline">READ MORE <span class="arrow-dot"></span></a>
</section>
<div class="abs welcome-photo" role="img" aria-label="Developer working at a computer monitor with code"></div>

<section class="abs process">
  <svg width="1200" height="190" viewBox="0 0 1200 190">
    <defs><marker id="head" markerWidth="10" markerHeight="10" refX="8" refY="5" orient="auto"><path d="M0 0L10 5L0 10z" fill="#fff"/></marker></defs>
    <line x1="318" y1="80" x2="546" y2="80" stroke="#fff" stroke-width="3" marker-end="url(#head)"/>
    <line x1="648" y1="80" x2="874" y2="80" stroke="#fff" stroke-width="3" marker-end="url(#head)"/>
    <g fill="none" stroke="#fff">
      <circle cx="268" cy="80" r="48" stroke-width="3"/><circle cx="268" cy="80" r="40" fill="#fff" stroke="none"/><circle cx="268" cy="80" r="36" fill="#17232b" stroke="none"/>
      <circle cx="598" cy="80" r="48" stroke-width="3"/><circle cx="598" cy="80" r="40" fill="#fff" stroke="none"/><circle cx="598" cy="80" r="36" fill="#17232b" stroke="none"/>
      <circle cx="926" cy="80" r="48" stroke-width="3"/><circle cx="926" cy="80" r="40" fill="#fff" stroke="none"/><circle cx="926" cy="80" r="36" fill="#17232b" stroke="none"/>
    </g>
    <g fill="#fff">
      <path d="M268 62l20 8-20 8-20-8z"/><path d="M250 78l18 7 18-7 3 2-21 8-21-8z"/><path d="M250 86l18 7 18-7 3 2-21 8-21-8z"/>
      <rect x="582" y="86" width="6" height="12"/><rect x="592" y="80" width="6" height="18"/><rect x="602" y="84" width="6" height="14"/><rect x="612" y="76" width="6" height="22"/>
      <path d="M580 78l12-10 8 6 12-12" fill="none" stroke="#fff" stroke-width="3"/><path d="M606 60h9v9z"/>
      <path d="M912 80v18h28V80" fill="none" stroke="#fff" stroke-width="3"/><path d="M926 58l-10 10h7v16h6V68h7z"/>
    </g>
  </svg>
  <div class="step-label" style="left:188px">DATA</div>
  <div class="step-label" style="left:518px">ANALYSIS</div>
  <div class="step-label" style="left:846px">ACTION</div>
</section>

<h2 class="abs price-title">PRICE</h2>

<article class="abs plan plan-doc">
  <div class="plan-head">PRICE FOR DOC SECURE</div>
  <div class="plan-badge">
    <svg width="116" height="116" viewBox="-57 -57 114 114"><polygon fill="#d0300f" points="0,-56 8,-49 17,-53 22,-45 32,-46 33,-36 43,-33 40,-24 49,-18 43,-10 50,-2 42,4 47,13 38,17 40,27 30,29 29,39 19,38 13,47 5,42 -3,49 -10,42 -19,46 -23,37 -33,37 -32,27 -43,24 -39,15 -48,9 -41,2 -48,-6 -40,-12 -44,-21 -35,-25 -36,-35 -26,-37 -22,-46 -13,-42 -6,-50"/></svg>
    <span>$1,99</span>
  </div>
  <div class="per-month">Per Month</div>
  <ul>
    <li><svg width="13" height="13" viewBox="0 0 13 13"><rect width="13" height="13" fill="none" stroke="#d0300f"/><path d="M2 6l3 3 6-7" fill="none" stroke="#d0300f" stroke-width="2.5"/></svg>Lorem Ipsum is simply dummy text</li>
    <li><svg width="13" height="13" viewBox="0 0 13 13"><rect width="13" height="13" fill="none" stroke="#d0300f"/><path d="M2 6l3 3 6-7" fill="none" stroke="#d0300f" stroke-width="2.5"/></svg>Lorem Ipsum is simply dummy text</li>
    <li><svg width="13" height="13" viewBox="0 0 13 13"><rect width="13" height="13" fill="none" stroke="#d0300f"/><path d="M2 6l3 3 6-7" fill="none" stroke="#d0300f" stroke-width="2.5"/></svg>Lorem Ipsum is simply dummy text</li>
    <li><svg width="13" height="13" viewBox="0 0 13 13"><rect width="13" height="13" fill="none" stroke="#d0300f"/><path d="M2 6l3 3 6-7" fill="none" stroke="#d0300f" stroke-width="2.5"/></svg>Lorem Ipsum is simply dummy text</li>
  </ul>
  <div class="order-btn">Order Now<i><svg width="21" height="21" viewBox="0 0 16 16"><path d="M1 2h3l2 8h7l2-6H5" fill="none" stroke="#d0300f" stroke-width="2"/><circle cx="7" cy="13.5" r="1.5" fill="#d0300f"/><circle cx="12" cy="13.5" r="1.5" fill="#d0300f"/></svg></i></div>
</article>

<article class="abs plan plan-land">
  <div class="plan-head">PRICE FOR LAND SECURE</div>
  <div class="plan-badge">
    <svg width="116" height="116" viewBox="-57 -57 114 114"><polygon fill="#1a78c2" points="0,-56 8,-49 17,-53 22,-45 32,-46 33,-36 43,-33 40,-24 49,-18 43,-10 50,-2 42,4 47,13 38,17 40,27 30,29 29,39 19,38 13,47 5,42 -3,49 -10,42 -19,46 -23,37 -33,37 -32,27 -43,24 -39,15 -48,9 -41,2 -48,-6 -40,-12 -44,-21 -35,-25 -36,-35 -26,-37 -22,-46 -13,-42 -6,-50"/></svg>
    <span>$3,99</span>
  </div>
  <div class="per-month">Per Month</div>
  <ul>
    <li><svg width="13" height="13" viewBox="0 0 13 13"><rect width="13" height="13" fill="none" stroke="#1a78c2"/><path d="M2 6l3 3 6-7" fill="none" stroke="#1a78c2" stroke-width="2.5"/></svg>Lorem Ipsum is simply dummy text</li>
    <li><svg width="13" height="13" viewBox="0 0 13 13"><rect width="13" height="13" fill="none" stroke="#1a78c2"/><path d="M2 6l3 3 6-7" fill="none" stroke="#1a78c2" stroke-width="2.5"/></svg>Lorem Ipsum is simply dummy text</li>
    <li><svg width="13" height="13" viewBox="0 0 13 13"><rect width="13" height="13" fill="none" stroke="#1a78c2"/><path d="M2 6l3 3 6-7" fill="none" stroke="#1a78c2" stroke-width="2.5"/></svg>Lorem Ipsum is simply dummy text</li>
    <li><svg width="13" height="13" viewBox="0 0 13 13"><rect width="13" height="13" fill="none" stroke="#1a78c2"/><path d="M2 6l3 3 6-7" fill="none" stroke="#1a78c2" stroke-width="2.5"/></svg>Lorem Ipsum is simply dummy text</li>
  </ul>
  <div class="order-btn">Order Now<i><svg width="21" height="21" viewBox="0 0 16 16"><path d="M1 2h3l2 8h7l2-6H5" fill="none" stroke="#1a78c2" stroke-width="2"/><circle cx="7" cy="13.5" r="1.5" fill="#1a78c2"/><circle cx="12" cy="13.5" r="1.5" fill="#1a78c2"/></svg></i></div>
</article>

<section class="abs contact">
  <div class="contact-icon"><svg width="32" height="26" viewBox="0 0 32 26"><rect x="1" y="3" width="30" height="20" fill="#fff"/><path d="M1 3l15 11L31 3" fill="none" stroke="#1a78c2" stroke-width="2.5"/></svg></div>
  <h2>CONTACT FORM</h2>
  <div class="field f-name"><svg width="12" height="13" viewBox="0 0 12 13"><circle cx="6" cy="4" r="3.5" fill="#ddd"/><path d="M0 13c0-4 3-6 6-6s6 2 6 6z" fill="#ddd"/></svg>Enter your name</div>
  <div class="field f-phone"><svg width="14" height="12" viewBox="0 0 14 12"><rect width="14" height="11" fill="#ddd"/><path d="M0 1l7 5 7-5" fill="none" stroke="#333" stroke-width="1.5"/></svg>Enter your phone</div>
  <div class="field f-mail"><svg width="12" height="13" viewBox="0 0 12 13"><path d="M2 0l3 3-2 2c1 2 3 4 5 5l2-2 3 3-2 2C5 13-1 7 0 2z" fill="#ddd"/></svg>Enter your email</div>
  <div class="f-msg">Enter your message</div>
  <div class="submit">SUBMIT</div>
</section>

<footer class="abs site-footer">Copyright 2017 PlotwiseGuard All Rights Reserved</footer>

</body>
</html>
```